Business Card Design Project

Looking for a logo and business card for a Real State Business i will be opening. The name is not choosen yet , but will probably be RTV IMOVEIS.
I was thinking black and silver colors, but am open to nice ideas.
I did add a business card that i liked a lot, am looking for something like that, with logo in black or silver in a black card. The logo i was thinking in the letters RTV as i uploaded or something or little and cute buildings or a house...just ideas, can be any nice logo.
Updates

You guys can add other colors if you want, I like colors very "BRIGHT" and "open", like red, pink, strong colors. almost glow in the dark colors. lol

Designers,

I've increased more 88 dollars in the budget for 1st place cause I will want envelope designs... small and big sizes.

So 1st place is now U$248,00. 

No need to send the envelope designs right now... only the business cards designs.

Thank you.

Industry/Entity Type

Business

Requirements
Must have
• Renata Tavares Vilela

www.RTVimoveis-exemplo.com.br

+554188316402

renata@rtvimoveis-exemplo.com.br

```html
<!DOCTYPE html>
<html lang="pt-BR">
<head>
<meta charset="utf-8">
<title>RTV Imoveis — Cartão de visita</title>
<link rel="stylesheet" href="https://fonts.googleapis.com/css2?family=Jost:wght@300;400;700&display=swap">
<style>
  :root {
    --backdrop: #eceeed;
    --card: #1d1d1b;
    --accent: #f39c1a;
    --ink-light: #f2f2f2;
    --ink-muted: #bdbdbd;
    --shadow: rgba(0, 0, 0, 0.35);
  }
  * { margin: 0; padding: 0; box-sizing: border-box; }
  html, body {
    width: 1200px;
    height: 642px;
    overflow: hidden;
    background: var(--backdrop);
    font-family: "Jost", sans-serif;
  }
  .stage { position: relative; width: 1200px; height: 642px; }
  .card {
    position: absolute;
    top: 148px;
    height: 276px;
    background: var(--card);
    box-shadow: 0 3px 8px var(--shadow);
  }
  .card--front { left: 120px; width: 478px; }
  .card--back { left: 629px; width: 475px; height: 275px; }

  .brand {
    position: absolute;
    left: 0;
    right: 0;
    top: 78px;
    display: flex;
    flex-direction: column;
    align-items: center;
  }
  .brand__mark {
    width: 16px;
    height: 16px;
    background: var(--accent);
    margin-bottom: 70px;
  }
  .brand__name {
    color: var(--ink-light);
    font-weight: 300;
    font-size: 21px;
    letter-spacing: 4.5px;
    line-height: 1;
    padding-left: 4.5px;
  }

  .contact {
    position: absolute;
    left: 152px;
    top: 96px;
    text-transform: uppercase;
  }
  .contact__name {
    color: var(--ink-light);
    font-weight: 700;
    font-size: 12px;
    letter-spacing: 1.2px;
    line-height: 14px;
    padding-bottom: 2px;
    border-bottom: 2px solid var(--accent);
    display: inline-block;
    margin-bottom: 7px;
  }
  .contact__line {
    color: var(--ink-muted);
    font-weight: 400;
    font-size: 10.5px;
    letter-spacing: 1px;
    line-height: 17.5px;
    font-style: normal;
  }
</style>
</head>
<body>
  <main class="stage">
    <section class="card card--front" aria-label="Frente do cartão">
      <div class="brand">
        <span class="brand__mark" aria-hidden="true"></span>
        <span class="brand__name">RTV IMOVEIS</span>
      </div>
    </section>

    <section class="card card--back" aria-label="Verso do cartão">
      <div class="contact">
        <p class="contact__name">Renata Tavares Vilela</p>
        <address>
          <p class="contact__line">www.RTVimoveis-exemplo.com.br</p>
          <p class="contact__line">+554188316402</p>
          <p class="contact__line">renata@rtvimoveis-exemplo.com.br</p>
        </address>
      </div>
    </section>
  </main>
</body>
</html>
```